Web Design Project for velbrook

We are looking for a sleek and sophisticated website design for our already developed web-based gallery management software application. Here is a link to our web-app: http://www.vel-brook.co

You will login on the main page and then we would like to include all of the information on the PDF that I am providing below (it outlines what?, where?, why? who? and how much?). Basically, we need a home page, about page, and a pricing page, as well as a sign up page that should be navigable from the upper right hand corner of the site where the sign in/sign up would be located. Also, our 3 tenets are that the software program is "attractive, accessible, and affordable", which might need to be somehow incorporated. There are a few websites that we would like for you to take inspiration from listed below:

https://tidemoxen.com (for homepage)
https://plumwovenly.com (for homepage/pricing page/etc)
https://tidemoxen.com/tour (for a tour of how the product works)

We are currently having a logo designed and will share that as soon as it is available! Also, let us know if you need photos/screen shots, as we can provide them.

Thanks!

Reason: Extending deadline as we are just now getting designs we would like to see fully developed.

Target Market(s)

art galleries, artists, art collectors, art consultants, museums

Industry/Entity Type

Software

Requirements
Must have
• Home page
About page (or tour through the app)
Pricing page
Sign up page (the more click-throughs to signing up the better)

```html
<!DOCTYPE html>
<html lang="en">
<head>
<meta charset="utf-8">
<title>velbrook — gallery management in the cloud</title>
<link rel="stylesheet" href="https://fonts.googleapis.com/css2?family=Arimo:wght@400;700&family=Cutive+Mono&family=Comfortaa:wght@400&display=swap">
<style>
  :root {
    --teal: #3aa9c2;
    --teal-btn: #45b3c6;
    --ink: #2b2b2b;
    --text: #4a4a4a;
    --muted: #777;
    --dot: #bdbdbd;
    --footer: #353535;
    --footer-text: #e8e8e8;
    --nav-bg: rgba(40, 40, 40, 0.72);
    --page: #ffffff;
  }
  * { box-sizing: border-box; margin: 0; padding: 0; }
  html, body { width: 1200px; height: 1200px; overflow: hidden; background: var(--page); }
  body { position: relative; font-family: "Arimo", Arial, sans-serif; color: var(--text); }
  .abs { position: absolute; }

  /* Hero */
  .hero { left: 180px; top: 0; width: 807px; height: 540px; overflow: hidden;
    background: linear-gradient(100deg, #d9d6cf 0%, #c4c1ba 30%, #8d8a84 55%, #4a5566 72%, #c9c7c1 100%); }
  .hero-photo { position: absolute; inset: 0;
    background: radial-gradient(ellipse 200px 330px at 560px 330px, rgba(44,58,82,0.85), rgba(44,58,82,0) 100%),
                radial-gradient(ellipse 120px 80px at 90px 380px, rgba(60,60,60,0.35), rgba(0,0,0,0)); }
  .brand { left: 28px; top: 20px; display: flex; align-items: center; gap: 8px; }
  .brand-dot { width: 22px; height: 22px; border: 3px solid var(--teal); border-radius: 50%; }
  .brand-name { font-family: "Comfortaa", sans-serif; font-size: 17px; color: var(--teal); }
  .nav { left: 442px; top: 7px; width: 365px; height: 25px; background: var(--nav-bg);
    font-family: "Cutive Mono", monospace; font-variant: small-caps; color: #eee; }
  .nav a { position: absolute; top: 4px; color: inherit; text-decoration: none; font-size: 15px; letter-spacing: 1.5px; }
  .nav .login { font-size: 10px; top: 8px; letter-spacing: 1px; }
  .quote { left: 59px; top: 140px; font-family: "Cutive Mono", monospace; font-variant: small-caps;
    font-size: 17px; line-height: 15px; letter-spacing: 2.6px; color: #1e1e1e; }
  .attribution { left: 60px; top: 237px; font-family: "Cutive Mono", monospace; font-variant: small-caps;
    font-size: 14px; letter-spacing: 1.5px; color: #1e1e1e; }
  .btn-hero { top: 272px; height: 30px; background: var(--teal-btn); color: #fff;
    font-family: "Cutive Mono", monospace; font-variant: small-caps; font-size: 15px; letter-spacing: 2px;
    display: flex; align-items: center; justify-content: center; }

  /* Content */
  .heading { font-size: 18px; color: var(--ink); letter-spacing: -0.6px; }
  .rule { border-top: 1px dotted var(--dot); height: 0; }
  .intro { left: 239px; top: 611px; width: 356px; font-size: 12.6px; line-height: 18.2px; color: var(--text); letter-spacing: -0.2px; }
  .devices { left: 286px; top: 710px; }
  .device-note { left: 246px; top: 786px; font-size: 12px; line-height: 15.5px; letter-spacing: -0.5px; color: var(--text); }
  .app-shot { left: 233px; top: 837px; width: 349px; height: 181px; border: 1px solid #cfcfcf;
    box-shadow: 0 1px 4px rgba(0,0,0,0.25);
    background: linear-gradient(180deg, #e2e2e2 0, #e2e2e2 14px, #f7f7f7 14px, #ffffff 100%); }
  .divider { left: 634px; top: 603px; height: 352px; border-left: 1px dotted var(--dot); }
  .perk-icon { top: 628px; width: 62px; height: 62px; border: 1px solid #444; border-radius: 50%; display: flex; align-items: center; justify-content: center; }
  .perk-label { top: 702px; font-size: 14px; color: var(--ink); letter-spacing: -0.6px; }
  .btn-signup { left: 742px; top: 732px; width: 115px; height: 33px; background: var(--teal-btn); color: #fff;
    font-size: 18px; letter-spacing: -0.8px; display: flex; align-items: center; justify-content: center; }
  .faq { left: 671px; top: 851px; width: 220px; font-size: 10px; line-height: 15px; letter-spacing: -0.5px; color: #222; }
  .faq-item { margin-bottom: 7px; }
  .faq-answer { color: var(--teal); }

  /* Footer */
  .footer { left: 180px; top: 1057px; width: 807px; height: 143px; background: var(--footer); color: var(--footer-text); }
  .foot-links { top: 33px; font-size: 9.5px; line-height: 15px; letter-spacing: -0.4px; list-style: none; }
  .foot-title { top: 30px; font-size: 11.5px; letter-spacing: -0.4px; text-align: center; border-bottom: 1px solid #aaa; padding-bottom: 1px; }
  .email-field { left: 480px; top: 51px; width: 101px; height: 19px; background: #d8d8d8; color: #8a8a8a; font-size: 11px; display: flex; align-items: center; justify-content: center; letter-spacing: -0.4px; }
  .subscribe { left: 494px; top: 75px; font-size: 11.5px; letter-spacing: -0.4px; }
  .follow { left: 639px; top: 49px; font-size: 9px; letter-spacing: -0.4px; }
  .follow span { color: var(--teal); }
  .foot-brand { left: 348px; top: 84px; width: 110px; text-align: center; font-family: "Comfortaa", sans-serif; font-size: 18px; color: #fff; }
  .copyright { left: 300px; top: 128px; width: 204px; text-align: center; font-size: 9px; letter-spacing: -0.4px; }
</style>
</head>
<body>

<header class="hero abs">
  <div class="hero-photo" role="img" aria-label="Photo of a young art student in a blue leather jacket holding a tablet on a blurred city street"></div>
  <div class="brand abs"><span class="brand-dot"></span><span class="brand-name">velbrook</span></div>
  <nav class="nav abs">
    <a style="left:23px">Home</a>
    <a style="left:77px">About</a>
    <a style="left:139px">Pricing</a>
    <a class="login" style="left:254px">login ▾</a>
  </nav>
  <blockquote class="quote abs">“I can now view my friends<br>art gallery anytime at low cost.<br>It is much easier to manage since<br>I can acces to it not only with my<br>PC but also on my phone and tablet.”</blockquote>
  <p class="attribution abs">Milo. Art student</p>
  <a class="btn-hero abs" style="left:65px;width:102px">Learn more</a>
  <a class="btn-hero abs" style="left:183px;width:102px">Try it now</a>
</header>

<main>
  <h2 class="heading abs" style="left:238px;top:571px">What is velbrook?</h2>
  <div class="rule abs" style="left:238px;top:603px;width:356px"></div>
  <p class="intro abs">velBROOK is one of the only truly web-based gallery management software systems currently available for galleries, artists, consultants and collectors. On a basic level, it allows you to manage your artists, art inventory, clients, and invoices in one clean interface that is highly integrated.</p>

  <svg class="devices abs" width="220" height="65" viewBox="0 0 220 65" aria-hidden="true">
    <rect x="3" y="3" width="68" height="48" fill="none" stroke="#3a3a3a" stroke-width="4"/>
    <path d="M24 62 Q37 46 50 62 Z" fill="#3a3a3a"/>
    <rect x="77" y="3" width="20" height="59" fill="#3a3a3a"/>
    <line x1="81" y1="12" x2="93" y2="12" stroke="#fff" stroke-width="1"/>
    <line x1="81" y1="16" x2="93" y2="16" stroke="#fff" stroke-width="1"/>
    <line x1="81" y1="20" x2="93" y2="20" stroke="#fff" stroke-width="1"/>
    <circle cx="87" cy="46" r="1.5" fill="#fff"/>
    <rect x="121" y="6" width="42" height="55" rx="2" fill="none" stroke="#3a3a3a" stroke-width="4"/>
    <circle cx="142" cy="58" r="1.3" fill="#3a3a3a"/>
    <rect x="185" y="17" width="30" height="45" rx="4" fill="none" stroke="#3a3a3a" stroke-width="4"/>
    <line x1="186" y1="54" x2="214" y2="54" stroke="#3a3a3a" stroke-width="2"/>
  </svg>
  <p class="device-note abs">velBROOK can be viewed on your mobile phone/tablet device.<br>velBROOK is the easiest way to manage your art data on the cloud.</p>

  <div class="app-shot abs" role="img" aria-label="Screenshot of the web app's Artwork List screen with a video player overlay"></div>

  <div class="divider abs"></div>

  <h2 class="heading abs" style="left:683px;top:571px">Why choose velbrook?</h2>
  <div class="rule abs" style="left:672px;top:603px;width:280px"></div>

  <div class="perk-icon abs" style="left:670px">
    <svg width="36" height="36" viewBox="0 0 36 36" aria-hidden="true"><path d="M6 20 V17 A12 12 0 0 1 30 17 V20" fill="none" stroke="#222" stroke-width="3"/><rect x="3" y="18" width="7" height="10" rx="2" fill="#222"/><rect x="26" y="18" width="7" height="10" rx="2" fill="#222"/><path d="M30 27 Q28 33 20 33" fill="none" stroke="#222" stroke-width="2"/></svg>
  </div>
  <div class="perk-icon abs" style="left:764px">
    <svg width="30" height="40" viewBox="0 0 30 40" aria-hidden="true"><path d="M15 2 L28 18 H20 V38 H10 V18 H2 Z" fill="#222"/></svg>
  </div>
  <div class="perk-icon abs" style="left:853px">
    <svg width="36" height="36" viewBox="0 0 36 36" aria-hidden="true"><ellipse cx="18" cy="26" rx="12" ry="4" fill="none" stroke="#222" stroke-width="2"/><ellipse cx="18" cy="19" rx="12" ry="4" fill="none" stroke="#222" stroke-width="2"/><ellipse cx="18" cy="12" rx="12" ry="4" fill="none" stroke="#222" stroke-width="2"/></svg>
  </div>
  <span class="perk-label abs" style="left:659px">Free Support</span>
  <span class="perk-label abs" style="left:753px">Free Upgrade</span>
  <span class="perk-label abs" style="left:854px">Affordable</span>
  <a class="btn-signup abs">Sign up now</a>

  <h2 class="heading abs" style="left:690px;top:800px">Frequently Asked Questions</h2>
  <div class="rule abs" style="left:672px;top:839px;width:280px"></div>
  <div class="faq abs">
    <div class="faq-item">1. Lorem ipsum dolor sit amet, et pulvinar lacinia, tellus erat interdum anteconsectetur adipiscing elit?<br><span class="faq-answer">- Maecenas 29$ ut lacus vitae velit gravida tristique vitae velit gravida.</span></div>
    <div class="faq-item">2. Etiam dictum pharetra turpis quis malesuada?<br><span class="faq-answer">- Aenean sagittis lectus arcu, lacinia vulputate ipsum condimentum quis.</span></div>
    <div class="faq-item">3. Morbi tincidunt molestie massa?<br><span class="faq-answer">- Phasellus suscipit bibendum justo et porta. Vestibulum ante ipsum primis in faucibus orci</span></div>
  </div>
</main>

<footer class="footer abs">
  <ul class="foot-links abs" style="left:58px"><li>Home</li><li>About us</li><li>Contact us</li></ul>
  <ul class="foot-links abs" style="left:144px"><li>FAQ</li><li>Blog</li><li>Sitemap</li></ul>
  <ul class="foot-links abs" style="left:221px"><li>Community &amp; Feedback</li><li>Privacy</li><li>Help &amp; Support</li></ul>
  <div class="foot-title abs" style="left:482px;width:97px">Newsletter</div>
  <div class="email-field abs">name@inbox.test</div>
  <div class="subscribe abs">Subscribe now</div>
  <div class="foot-title abs" style="left:639px;width:128px">Connect with us</div>
  <div class="follow abs">Follow us on <span>Skylark</span> or <span>Hearthnet</span></div>
  <div class="foot-brand abs">velbrook</div>
  <div class="copyright abs">© 2013 velBROOK All rights reserved.</div>
</footer>

</body>
</html>
```